Business Card Design

Hi I need a business card designed, we already have the business name logo artwork and would like some concept ideas for the Bus Card layout.
On the back of the card i want to include the products and services that we offer.
We are a Plastics Sheeting manufacture based in Perth Australia.

                                       

We need a BC design for a company called Tarnby Plastics based in Perth Australia.

We supply from DIY to Trade & Industrial  Engineering Markets.

We specialise in:

·         Cut to size panels  (all shapes and sizes)

·         Plastics fabrication & Welding

·         Custom Designs

·         Plastic Repairs

·         PVC Pipe Slotting & PVC Pipe Threading

·         Supplier of all types of engineering plastics and profiles.

Including:           Acrylic / Vendrix

                               Polycarbonate / Moravite

                               Prismatic Light Diffuser

                               Tubrasin

                               HDPE / UHMWPE

                               PVC / PVC Foam

                               Nylon

                               HIPS

```html
<!DOCTYPE html>
<html lang="en">
<head>
<meta charset="utf-8">
<title>Tarnby Plastics – Business Card</title>
<link href="https://fonts.googleapis.com/css2?family=Open+Sans:wght@400;600;700&display=swap" rel="stylesheet">
<style>
  :root {
    --navy: #1b2a63;
    --blue: #2f86c6;
    --orange: #f3a21b;
    --ink: #3b3b3b;
    --white: #ffffff;
    --stage: #e9e6e1;
    --rule-light: #9aa3b5;
    --rule-dark: #6f7ba3;
  }
  * { box-sizing: border-box; margin: 0; padding: 0; }
  html, body {
    width: 1200px; height: 720px; overflow: hidden;
    background: var(--stage);
    font-family: 'Open Sans', sans-serif;
  }
  .stage { position: relative; width: 1200px; height: 720px; }

  .card {
    position: absolute; top: 200px;
    width: 560px; height: 320px;
    overflow: hidden;
    box-shadow: 0 6px 18px rgba(0,0,0,.18);
  }
  .card--front { left: 30px; background: var(--white); }
  .card--back  { left: 610px; background: var(--navy); color: var(--white); }

  /* wordmark */
  .wordmark {
    position: absolute; left: 0; right: 0;
    display: flex; align-items: center; justify-content: center; gap: 10px;
    font-weight: 700; letter-spacing: .5px; white-space: nowrap;
  }
  .wordmark__square { width: 22px; height: 22px; }
  .card--front .wordmark { top: 40px; font-size: 44px; color: var(--navy); }
  .card--front .wordmark__square { background: var(--navy); }
  .card--back .wordmark { top: 26px; font-size: 42px; color: var(--white); }
  .card--back .wordmark__square { background: var(--white); }

  /* front details */
  .person { position: absolute; top: 132px; right: 290px; text-align: right; }
  .person__name { font-size: 16px; font-weight: 700; color: var(--navy); }
  .person__title { font-size: 13px; font-weight: 600; color: var(--orange); margin-top: -2px; }
  .person__address { margin-top: 4px; font-size: 12.5px; line-height: 1.3; color: var(--ink); }

  .divider { position: absolute; width: 1px; background: var(--rule-light); }
  .card--front .divider { left: 282px; top: 118px; height: 118px; }

  .contact {
    position: absolute; top: 120px; left: 296px;
    list-style: none; font-size: 12.5px; color: var(--ink); line-height: 1.45;
  }
  .contact__item { display: flex; align-items: center; gap: 6px; }
  .contact__icon { width: 13px; height: 13px; flex: none; }
  .contact__legal { margin-top: 6px; font-size: 12px; line-height: 1.35; }

  .swoosh { position: absolute; left: 0; bottom: 0; width: 560px; height: 120px; }

  /* back */
  .tagline {
    position: absolute; top: 96px; left: 0; right: 0;
    text-align: center; font-size: 13.5px; font-weight: 700; line-height: 1.3;
  }
  .card--back .divider { left: 336px; top: 140px; height: 150px; background: var(--rule-dark); }
  .offer { position: absolute; top: 142px; }
  .offer--services { left: 26px; width: 300px; }
  .offer--materials { left: 352px; width: 200px; }
  .offer__heading { font-size: 16px; font-weight: 700; color: var(--orange); margin-bottom: 4px; }
  .offer__list { list-style: none; font-size: 12.5px; line-height: 1.4; }
  .offer__list li { position: relative; padding-left: 13px; }
  .offer__list li::before,
  .offer__dot::before {
    content: ""; position: absolute; left: 0; top: 7px;
    width: 6px; height: 6px; border-radius: 50%; background: var(--orange);
  }
  .offer__dot { position: relative; padding-left: 11px; margin-left: 8px; }
</style>
</head>
<body>
<main class="stage">

  <section class="card card--front" aria-label="Business card front">
    <div class="wordmark"><span class="wordmark__square"></span>Tarnby Plastics</div>

    <div class="person">
      <p class="person__name">Your Name</p>
      <p class="person__title">Title</p>
      <p class="person__address">
        Unit 4/18 Harlow Crescent<br>
        Kelmore Vale WA 6162<br>
        PO Box 2240<br>
        Kelmore Vale DC WA 6983
      </p>
    </div>

    <span class="divider"></span>

    <ul class="contact">
      <li class="contact__item">
        <svg class="contact__icon" viewBox="0 0 16 16"><circle cx="8" cy="8" r="8" fill="#f3a21b"/><path d="M5 4.5l1.6-.3.8 2-1 .8a5 5 0 0 0 2.6 2.6l.8-1 2 .8-.3 1.6C8 11.3 4.7 8 5 4.5z" fill="#fff"/></svg>
        08 9300 4127
      </li>
      <li class="contact__item">
        <svg class="contact__icon" viewBox="0 0 16 16"><circle cx="8" cy="8" r="8" fill="#f3a21b"/><rect x="5.5" y="3.5" width="5" height="9" rx="1" fill="#fff"/><rect x="6.5" y="4.8" width="3" height="5" fill="#f3a21b"/></svg>
        123-456-7890
      </li>
      <li class="contact__item">
        <svg class="contact__icon" viewBox="0 0 16 16"><circle cx="8" cy="8" r="8" fill="#f3a21b"/><rect x="4" y="7" width="8" height="4.5" fill="#fff"/><rect x="5.5" y="4" width="5" height="3" fill="#fff"/></svg>
        08 9300 4128
      </li>
      <li class="contact__item">
        <svg class="contact__icon" viewBox="0 0 16 16"><circle cx="8" cy="8" r="8" fill="#f3a21b"/><rect x="4" y="5" width="8" height="6" fill="#fff"/><path d="M4 5l4 3.3L12 5" fill="none" stroke="#f3a21b" stroke-width="1"/></svg>
        sales@tarnbyplastics.com.au
      </li>
      <li class="contact__legal">
        Brenlow Holdings Pty Ltd<br>
        T/A Tarnby Plastics ABN: TBA
      </li>
    </ul>

    <svg class="swoosh" viewBox="0 0 560 120" preserveAspectRatio="none" aria-hidden="true">
      <path d="M0 70 C150 120 330 110 560 30 L560 120 L0 120 Z" fill="#2f86c6"/>
      <path d="M0 84 C160 128 340 118 560 44 L560 120 L0 120 Z" fill="#ffffff"/>
      <path d="M0 90 C170 130 350 122 560 52 L560 120 L0 120 Z" fill="#1b2a63"/>
    </svg>
  </section>

  <section class="card card--back" aria-label="Business card back">
    <div class="wordmark"><span class="wordmark__square"></span>Tarnby Plastics</div>

    <p class="tagline">
      The Products And Services That We Offer<br>
      Are Supplied From DIY To Trade &amp; Industrial Engineering Markets
    </p>

    <div class="offer offer--services">
      <h2 class="offer__heading">We specialise in:</h2>
      <ul class="offer__list">
        <li>Cut to size panels (all shapes and sizes)</li>
        <li>Plastics fabrication &amp; Welding</li>
        <li>Custom Designs</li>
        <li>Plastic Repairs</li>
        <li>PVC Pipe Slotting &amp; PVC Pipe Threading</li>
        <li>Supplier of all types of engineering plastics and profiles</li>
      </ul>
    </div>

    <span class="divider"></span>

    <div class="offer offer--materials">
      <h2 class="offer__heading">Including:</h2>
      <ul class="offer__list">
        <li>Acrylic / Vendrix</li>
        <li>Polycarbonate / Moravite</li>
        <li>Prismatic Light Diffuser</li>
        <li>Tubrasin<span class="offer__dot">HDPE / UHMWPE</span></li>
        <li>PVC / PVC Foam</li>
        <li>Nylon<span class="offer__dot">HIPS</span></li>
      </ul>
    </div>
  </section>

</main>
</body>
</html>
```